Business Cards Design for the electrical wholesaler: clean bold dynamic :)

We need a business card design that would follow our latest brand guidelines. As an electrical wholesaler we want to bring a fresh look and feel into the industry. The design should be clean bold and dynamic. It should come alive with the renewed energy of our green colour. Our grey colour should keep things balanced and complement the notion of maturity and responsibility. We employ Lato as a corporate font however are not bound by this font and we’re open to interpretation here.

Target Market(s)

Electrical contractors

Industry/Entity Type

Business

Contact Information for Business Card

Logo
Name & Surname: Olena Dovbush
Job Title: Director of Marketing
Email: helen.dovbush@mailvane.example
Cell phone: XXX.XXX.XXXX
Address: 20917 - 87 Ave. Edmonton, AB, Canada. T6K 2R8
Business Phone: 780.555.0187
Website: www.qorvil.example

Font styles to use
Other font styles liked:
• Lato

Requirements
Must have
• Logo & website
Nice to have
• Brand elements - some of them you may find in the attached Brand Guidelines (e.g. three lines on the background signifying "W")

```html
<!DOCTYPE html>
<html lang="en">
<head>
<meta charset="utf-8">
<title>Qorvil Business Card</title>
<link rel="stylesheet" href="https://fonts.googleapis.com/css2?family=Lato:ital,wght@0,300;0,400;0,700;1,300&display=swap">
<style>
  :root {
    --brand-green: #8cc63f;
    --brand-grey: #4d4d4f;
    --text-grey: #58585a;
    --muted-grey: #9a9a9c;
    --canvas-bg: #ececec;
    --card-bg: #ffffff;
  }
  * { box-sizing: border-box; margin: 0; padding: 0; }
  html, body {
    width: 1200px; height: 1200px; overflow: hidden;
    background: var(--canvas-bg);
    font-family: "Lato", Arial, sans-serif;
  }
  .canvas {
    position: relative; width: 1200px; height: 1200px;
    display: flex; flex-direction: column; align-items: center; justify-content: center; gap: 56px;
  }
  .card {
    position: relative; width: 900px; height: 524px;
    background: var(--card-bg); border-radius: 16px;
    box-shadow: 0 2px 6px rgba(0,0,0,0.18);
    overflow: hidden;
  }
  .wordmark {
    position: absolute; left: 0; right: 0;
    display: flex; align-items: center; justify-content: center; gap: 18px;
  }
  .wordmark-square {
    width: 68px; height: 68px; background: var(--brand-green);
  }
  .wordmark-name {
    font-weight: 400; font-size: 104px; line-height: 1; color: var(--brand-grey);
    letter-spacing: -1px;
  }
  .card-front .wordmark { top: 142px; }
  .divider {
    position: absolute; left: 449px; width: 2px; background: var(--brand-green);
  }
  .divider-top { top: 0; height: 128px; }
  .divider-bottom { top: 368px; height: 152px; }
  .person {
    position: absolute; top: 282px; left: 0; right: 0; text-align: center;
    padding-left: 140px;
  }
  .person-name {
    font-weight: 700; font-size: 36px; color: var(--text-grey); line-height: 1.1;
  }
  .person-title {
    font-weight: 300; font-style: italic; font-size: 18px; color: var(--muted-grey);
    margin-top: 4px; padding-right: 60px;
  }
  .address {
    position: absolute; top: 410px; right: 474px; text-align: right;
    font-size: 19px; line-height: 26px; color: var(--text-grey);
  }
  .contacts {
    position: absolute; top: 380px; left: 478px; list-style: none;
  }
  .contact {
    display: flex; align-items: center; gap: 16px; height: 38px;
    font-size: 20px; color: var(--text-grey);
  }
  .contact-tag { width: 40px; height: 26px; flex: none; }
  .card-back .wordmark { top: 176px; }
  .back-website {
    position: absolute; top: 304px; left: 0; right: 0; text-align: center;
    font-size: 29px; letter-spacing: 7px; color: var(--text-grey);
  }
</style>
</head>
<body>
<main class="canvas">
  <section class="card card-front" aria-label="Business card front">
    <span class="divider divider-top"></span>
    <div class="wordmark">
      <span class="wordmark-square"></span>
      <span class="wordmark-name">qorvil</span>
    </div>
    <span class="divider divider-bottom"></span>
    <div class="person">
      <p class="person-name">Olena Dovbush</p>
      <p class="person-title">Director of Marketing</p>
    </div>
    <p class="address">20917 - 87 Ave. Edmonton, AB,<br>Canada. T6K 2R8</p>
    <ul class="contacts">
      <li class="contact">
        <svg class="contact-tag" viewBox="0 0 40 26" aria-hidden="true">
          <polygon points="0,0 28,0 40,13 28,26 0,26" fill="var(--brand-green)"/>
          <path d="M9 6c1-1 2-1 3 0l2 3c.5 1 0 2-1 2.5c1 2 2.5 3.5 4.5 4.5c.5-1 1.5-1.5 2.5-1l3 2c1 1 1 2 0 3c-2 2-5 1-9-2.5S7 8 9 6z" fill="none" stroke="#fff" stroke-width="1.5"/>
        </svg>
        <span>780.555.0187</span>
      </li>
      <li class="contact">
        <svg class="contact-tag" viewBox="0 0 40 26" aria-hidden="true">
          <polygon points="0,0 28,0 40,13 28,26 0,26" fill="var(--brand-green)"/>
          <rect x="7" y="7" width="17" height="12" fill="none" stroke="#fff" stroke-width="1.5"/>
          <polyline points="7,7 15.5,14 24,7" fill="none" stroke="#fff" stroke-width="1.5"/>
        </svg>
        <span>helen.dovbush@mailvane.example</span>
      </li>
      <li class="contact">
        <svg class="contact-tag" viewBox="0 0 40 26" aria-hidden="true">
          <polygon points="0,0 28,0 40,13 28,26 0,26" fill="var(--brand-green)"/>
          <circle cx="15.5" cy="13" r="8" fill="none" stroke="#fff" stroke-width="1.5"/>
          <ellipse cx="15.5" cy="13" rx="3.5" ry="8" fill="none" stroke="#fff" stroke-width="1.2"/>
          <line x1="7.5" y1="13" x2="23.5" y2="13" stroke="#fff" stroke-width="1.2"/>
        </svg>
        <span>www.qorvil.example</span>
      </li>
    </ul>
  </section>

  <section class="card card-back" aria-label="Business card back">
    <div class="wordmark">
      <span class="wordmark-square"></span>
      <span class="wordmark-name">qorvil</span>
    </div>
    <p class="back-website">www.qorvil.example</p>
  </section>
</main>
</body>
</html>
```